Startup company business card (Media & Advertising)

we need a business card design for a company that is a startup in the media and aggregation industry. Card needs to look funky and of a new breed/modern and upmarket.

Target Market(s)

advertisers/ brand agencies & media publishers

Industry/Entity Type

Advertising

Contact Information for Business Card

Please ensure the front face signifies our brand (plumvexo.com) and back has details for the contact. Standard contact such as phone , address, email , website etc.

Font styles to use
Other font styles liked:
• use styleguide and logo font and color

Colors

Designer to choose colors to be used in the design.

Requirements
Must have
• We are disrupting the media and agency industry so subtlety would be good to use imagery to signify this
Nice to have
• Please use logo colors for branding
Should not have
• be as creative and provide few options. Pick a brand color from logo and styleguide

```html
<!DOCTYPE html>
<html lang="en">
<head>
<meta charset="utf-8">
<title>plumvexo business card</title>
<link rel="stylesheet" href="https://fonts.googleapis.com/css2?family=Roboto:wght@400;500;700&display=swap">
<style>
  :root {
    --backdrop: #3a3a3a;
    --card-dark: #0b0b0b;
    --card-light: #ffffff;
    --brand-red: #e8344a;
    --ink: #333333;
    --ink-soft: #2a2a2a;
    --on-dark: #ffffff;
  }
  * { box-sizing: border-box; margin: 0; padding: 0; }
  html, body {
    width: 1200px; height: 896px; overflow: hidden;
    background: var(--backdrop);
    font-family: "Roboto", Arial, sans-serif;
  }
  .stage {
    position: relative; width: 1200px; height: 896px;
    display: flex; align-items: center; justify-content: center; gap: 40px;
  }
  .card {
    width: 540px; height: 309px; border-radius: 22px;
    position: relative; overflow: hidden;
  }
  .card--front { background: var(--card-dark); display: flex; align-items: center; justify-content: center; }
  .card--back { background: var(--card-light); }
  .brand {
    display: flex; align-items: center; gap: 14px;
    font-weight: 700; letter-spacing: 0.5px;
  }
  .brand__dot { width: 34px; height: 34px; border-radius: 50%; background: var(--brand-red); flex: none; }
  .brand__name { font-size: 48px; line-height: 1; }
  .card--front .brand__name { color: var(--on-dark); }
  .card--back .brand { position: absolute; left: 40px; top: 140px; }
  .card--back .brand__name { color: var(--ink); font-size: 40px; }
  .contact {
    position: absolute; left: 322px; top: 56px;
    color: var(--ink-soft); font-size: 13px; line-height: 1.55;
  }
  .contact__name { color: var(--brand-red); font-size: 19px; font-weight: 500; letter-spacing: 0.3px; }
  .contact__role { margin-bottom: 12px; }
  .contact__address { margin-bottom: 10px; }
  .contact__list { list-style: none; }
  .contact__list li { display: flex; align-items: center; gap: 8px; }
  .contact__list svg { width: 10px; height: 10px; fill: none; stroke: var(--brand-red); stroke-width: 1.6; flex: none; }
</style>
</head>
<body>
  <main class="stage">
    <section class="card card--front" aria-label="Card front">
      <div class="brand">
        <span class="brand__dot"></span>
        <span class="brand__name">plumvexo</span>
      </div>
    </section>

    <section class="card card--back" aria-label="Card back">
      <div class="brand">
        <span class="brand__dot"></span>
        <span class="brand__name">plumvexo</span>
      </div>
      <div class="contact">
        <p class="contact__name">DORIAN KESSLER</p>
        <p class="contact__role">Director</p>
        <p class="contact__address">2275 Harbor Lane<br>Delmont, WA 98402</p>
        <ul class="contact__list">
          <li>
            <svg viewBox="0 0 10 10" aria-hidden="true"><path d="M2 1 L4 3 L3 4.5 Q4.5 6.5 5.5 7 L7 6 L9 8 L8 9 Q4 9 1 4 Q1 2 2 1 Z"/></svg>
            +41795550183
          </li>
          <li>
            <svg viewBox="0 0 10 10" aria-hidden="true"><rect x="1" y="2.2" width="8" height="5.6"/><path d="M1 2.2 L5 5.5 L9 2.2"/></svg>
            info@plumvexo.com
          </li>
          <li>
            <svg viewBox="0 0 10 10" aria-hidden="true"><circle cx="5" cy="5" r="4"/><path d="M1 5 H9 M5 1 Q2.5 5 5 9 M5 1 Q7.5 5 5 9"/></svg>
            www.plumvexo.com
          </li>
        </ul>
      </div>
    </section>
  </main>
</body>
</html>
```